Meridel Hair Studio Needs a new appointment business card

We need a new appointment card for our hair salon.

I Dont want bright out there colours.
I would like it to be neat, clean, easy to read. White, Black, with a hint of colour if needed.

We need
-Logo
-Phone number 47208613
-Mobile Number: 0417306852
Address: Shop 3/214 Calder Road, The Elmgates, Kelsby 4812

BACK SIDE OF CARD
- Appointment Time & Date (White background so we are able to write on it)
(If you are unable to make your appointment please contact us ASAP 47208613)

I also would like the chatterly and Pictorama logo(Find us on Chatterly)(find us on Pictorama)

Target Market(s)

appointment card simple to read. all information for their next appoint For all our clients male and female

Industry/Entity Type

Hairdresser

Contact Information for Business Card

-Logo
-Phone number 47208613

BACK SIDE OF CARD

Font styles to use
Serif
Sans Serif
Script

Requirements
Must have
• White Back ground on backside with appointment deatils so we are able to write information (like appointment time and date)
Nice to have
• Find us on Chatterly
and
pictorama - meridel_hairstudio
Should not have
• BRIGHT COLOURS

```html
<!DOCTYPE html>
<html lang="en">
<head>
<meta charset="utf-8">
<title>Meridel Hair Studio – Appointment Card</title>
<link href="https://fonts.googleapis.com/css2?family=Montserrat:wght@400;500;600;700&display=swap" rel="stylesheet">
<style>
  :root {
    --backdrop: #2a2a2a;
    --card-white: #ffffff;
    --card-black: #0b0b0b;
    --ink: #111111;
    --paper-text: #ffffff;
    --rule: #222222;
  }
  * { box-sizing: border-box; margin: 0; padding: 0; }
  html, body {
    width: 1200px; height: 930px; overflow: hidden;
    background: var(--backdrop);
    font-family: "Montserrat", sans-serif;
  }
  .canvas { position: relative; width: 1200px; height: 930px; }

  .card {
    position: absolute;
    width: 560px; height: 340px;
    border-radius: 22px;
    overflow: hidden;
    box-shadow: 0 14px 30px rgba(0,0,0,.45);
  }

  /* Appointment side */
  .card--appointment { left: 70px; top: 90px; background: var(--card-white); color: var(--ink); }
  .card--appointment .wordmark { position: absolute; left: 0; right: 0; top: 62px; text-align: center; color: var(--ink); }
  .card--appointment .wordmark-rule { position: absolute; left: 190px; right: 70px; top: 130px; border-top: 1px solid var(--rule); }
  .appointment-row { position: absolute; left: 40px; right: 40px; display: flex; align-items: flex-end; gap: 6px; font-size: 15px; }
  .appointment-row .label { white-space: nowrap; }
  .appointment-row .blank { flex: 1; border-bottom: 1px solid var(--rule); height: 16px; }
  .row--date { top: 190px; }
  .row--date .label-main { font-weight: 600; font-size: 17px; }
  .row--time { top: 238px; }
  .row--time .blank { flex: 0 0 180px; }
  .row--time .contact { margin-left: 28px; font-weight: 700; font-size: 17px; white-space: nowrap; }

  /* Wordmark */
  .wordmark-name { display: block; font-weight: 600; font-size: 38px; letter-spacing: 3px; line-height: 1; }
  .wordmark-sub { display: block; font-weight: 600; font-size: 12px; letter-spacing: 5px; margin-top: 6px; }

  /* Contact side */
  .card--contact { left: 570px; top: 490px; background: linear-gradient(135deg, #1c1c1c 0%, var(--card-black) 55%); color: var(--paper-text); }
  .tool-illustration { position: absolute; left: 0; bottom: 0; width: 230px; height: 340px;
    background: linear-gradient(160deg, #ffffff 0%, #e6e6e6 100%);
    clip-path: polygon(0 22%, 40% 22%, 100% 100%, 0 100%); }
  .card--contact .wordmark { position: absolute; right: 40px; top: 56px; text-align: right; color: var(--paper-text); }
  .card--contact .wordmark-name { font-size: 34px; }
  .social-row { position: absolute; right: 40px; top: 150px; display: flex; gap: 8px; }
  .social-dot { width: 24px; height: 24px; border: 2px solid var(--paper-text); border-radius: 50%; }
  .contact-list { position: absolute; right: 40px; top: 192px; text-align: right; font-size: 15px; line-height: 24px; }
  .contact-line { display: flex; justify-content: flex-end; align-items: center; gap: 8px; white-space: nowrap; }
  .contact-line svg { width: 12px; height: 12px; fill: var(--paper-text); }
</style>
</head>
<body>
<main class="canvas">

  <section class="card card--appointment" aria-label="Appointment side">
    <div class="wordmark">
      <span class="wordmark-name">MERIDEL</span>
      <span class="wordmark-sub">HAIR-STUDIO</span>
    </div>
    <div class="wordmark-rule"></div>
    <div class="appointment-row row--date">
      <span class="label label-main">Appointment</span>
      <span class="blank"></span>
      <span class="label">Date:</span>
      <span class="blank"></span>
    </div>
    <div class="appointment-row row--time">
      <span class="label">Time:</span>
      <span class="blank"></span>
      <span class="contact">Contact us ASAP 47208613</span>
    </div>
  </section>

  <section class="card card--contact" aria-label="Contact side">
    <div class="tool-illustration" role="img" aria-label="Large black and white scissors illustration"></div>
    <div class="wordmark">
      <span class="wordmark-name">MERIDEL</span>
      <span class="wordmark-sub">HAIR-STUDIO</span>
    </div>
    <div class="social-row" aria-label="Find us on Chatterly and Pictorama">
      <span class="social-dot"></span>
      <span class="social-dot"></span>
    </div>
    <div class="contact-list">
      <div class="contact-line">47208613
        <svg viewBox="0 0 24 24" aria-hidden="true"><path d="M6.6 10.8a15 15 0 0 0 6.6 6.6l2.2-2.2a1 1 0 0 1 1-.25 11.4 11.4 0 0 0 3.6.57 1 1 0 0 1 1 1V20a1 1 0 0 1-1 1A17 17 0 0 1 3 4a1 1 0 0 1 1-1h3.5a1 1 0 0 1 1 1c0 1.25.2 2.45.57 3.57a1 1 0 0 1-.25 1z"/></svg>
      </div>
      <div class="contact-line">0417306852
        <svg viewBox="0 0 24 24" aria-hidden="true"><path d="M7 1h10a2 2 0 0 1 2 2v18a2 2 0 0 1-2 2H7a2 2 0 0 1-2-2V3a2 2 0 0 1 2-2zm0 3v14h10V4zm5 15.5a1 1 0 1 0 0 2 1 1 0 0 0 0-2z"/></svg>
      </div>
      <div class="contact-line">Shop 3/214 Calder Road,</div>
      <div class="contact-line">The Elmgates, Kelsby 4812</div>
    </div>
  </section>

</main>
</body>
</html>
```